Boutique Financial Services/Advisor Business Needs Web Design

Looking for an informational and functional web design for my Financial Services/Financial Advisement business. It should have functionality for Company name, address, phone #, "About Us", Who we are, Our Mission, Services we offer, Biographies/Photos of/about "The Team", and possibly a link to "Contact Us". Would like to see something new & exciting blended with a traditional/professional look that will appeal to those approaching retirement, as well as those younger clients that are beginning to think about planning for the future. I already have a web domain through HostMeadow, but would like this to be the design we use for that domain.
Financial Services/Financial Advisor
Coded - Design and coding required
1 page

```html
<!DOCTYPE html>
<html lang="en">
<head>
<meta charset="utf-8">
<title>Summitline Wealth Management</title>
<link rel="stylesheet" href="https://fonts.googleapis.com/css2?family=Cinzel:wght@400;500&family=Poppins:wght@400;500;600&display=swap">
<style>
:root{
  --navy:#0b0a4f;
  --navy-soft:#1b1a66;
  --grey:#f4f4f4;
  --line:#8a8a8a;
  --text:#3a3a3a;
  --white:#ffffff;
}
*{margin:0;padding:0;box-sizing:border-box}
html,body{width:1200px;height:4464px;overflow:hidden}
body{position:relative;font-family:"Poppins",sans-serif;color:var(--text);background:var(--white)}
.abs{position:absolute}
.serif{font-family:"Cinzel",serif;font-weight:400;color:var(--navy)}
.topbar{left:0;top:0;width:1200px;height:43px;background:var(--navy);color:#fff;font-size:14px}
.topbar .phone{left:69px;top:12px;display:flex;gap:10px;align-items:center}
.topbar .mail{right:69px;top:12px;display:flex;gap:10px;align-items:center}
.nav{left:0;top:43px;width:1200px;height:53px;background:#fff;font-size:13px;color:var(--navy)}
.nav a{position:absolute;top:21px;text-decoration:none;color:var(--navy)}
.nav a.active{font-weight:600}
.brand-badge{left:434px;top:0;width:356px;height:152px;z-index:3}
.brand-name{left:434px;top:62px;width:356px;text-align:center;z-index:4;font-family:"Cinzel",serif;color:var(--navy);font-size:21px;line-height:25px}
.hero{left:0;top:96px;width:1200px;height:754px;background:linear-gradient(100deg,#6f7a52 0%,#a9b08c 28%,#dfe6ee 45%,#f3f6fa 65%,#c9d3e2 100%)}
.hero-cut{left:0;top:96px;z-index:1}
.hero-text{left:416px;top:288px;width:780px;text-align:center;z-index:2;white-space:nowrap}
.hero-text .kicker{font-family:"Poppins",sans-serif;font-weight:600;font-size:35px;line-height:44px;color:var(--navy)}
.hero-text h1{font-family:"Cinzel",serif;font-weight:400;color:var(--navy);font-size:60px;line-height:79px;margin-top:6px}
.btn{position:absolute;display:flex;align-items:center;justify-content:center;gap:18px;background:var(--navy);color:#fff;border-radius:40px;font-weight:500;text-transform:uppercase;text-decoration:none}
.btn .dot{width:18px;height:18px;border-radius:50%;background:#fff;display:flex;align-items:center;justify-content:center}
.btn.light{background:#fff;color:var(--navy)}
.btn.light .dot{background:var(--navy)}
.scroll-dot{left:583px;top:806px;width:34px;height:34px;border-radius:50%;background:#fff;border:2px solid #9a9a9a;z-index:2;display:flex;align-items:center;justify-content:center}
.about-photo{left:95px;top:945px;width:482px;height:333px;background:linear-gradient(135deg,#3a3f4c,#9aa3ad 50%,#dfe3e8);clip-path:polygon(50% 0,100% 100%,0 100%)}
.sec-title{font-size:48px;line-height:52px}
.sec-sub{font-size:16px;color:var(--navy-soft);display:flex;align-items:center;gap:10px;text-transform:uppercase}
.sec-sub i{display:block;height:3px;background:var(--navy)}
.para{font-size:13.5px;line-height:26.7px;color:var(--text)}
.services-bg{left:0;top:1396px;z-index:0}
.diamond{width:240px;height:240px;transform:rotate(45deg);background:#fff;box-shadow:0 0 14px rgba(0,0,0,.12)}
.svc{width:300px;text-align:center;z-index:2}
.svc .icon{width:98px;height:98px;margin:0 auto;border-radius:50%;border:3px solid var(--navy);background:#fff;display:flex;align-items:center;justify-content:center}
.svc .icon span{width:80px;height:80px;border-radius:50%;background:var(--navy);display:flex;align-items:center;justify-content:center}
.svc h3{font-size:20px;font-weight:600;color:#1a1a1a;margin-top:16px}
.svc.dark .icon{border-color:#fff}
.svc.dark h3{color:#fff}
.card-hi{left:118px;top:2693px;width:239px;height:397px;background:#ececec}
.member{width:240px;text-align:center}
.hex{width:176px;height:200px;margin:0 auto;clip-path:polygon(50% 0,100% 25%,100% 75%,50% 100%,0 75%,0 25%);background:#e6e6e6;display:flex;align-items:center;justify-content:center}
.hex span{display:block;width:164px;height:188px;clip-path:polygon(50% 0,100% 25%,100% 75%,50% 100%,0 75%,0 25%);background:linear-gradient(180deg,#c8ccd2,#6b6f78)}
.member h4{font-size:21px;font-weight:600;color:var(--navy);margin-top:14px}
.member p{font-size:14px;margin-top:4px}
.member .soc{width:38px;height:38px;border-radius:50%;background:var(--navy);margin:14px auto 0;display:flex;align-items:center;justify-content:center}
.member .soc i{width:14px;height:14px;background:#fff;border-radius:2px}
.contact{left:0;top:3291px;width:1200px;height:870px;background:var(--navy)}
.field{background:#fff;font-size:11px;color:#999;padding:10px 18px;border:1px solid #ddd}
.footer-bg{left:0;top:4020px;z-index:1}
.footer{z-index:2}
.foot-title{font-family:"Cinzel",serif;font-size:21px;color:var(--navy)}
.links{list-style:none;font-size:13.5px;color:#222}
.links li{display:flex;align-items:center;gap:12px;height:26px}
.links li::before{content:"";width:7px;height:7px;border-radius:50%;background:var(--navy)}
.c-item{display:flex;gap:18px;font-size:13.5px;color:#222;line-height:17px}
.c-item b{font-weight:500}
.c-ico{width:22px;height:22px;background:var(--navy);border-radius:3px;flex:none}
.bottom{left:0;top:4410px;width:1200px;height:54px;background:var(--navy);color:#fff;font-size:12px;z-index:3}
.sq{width:25px;height:25px;background:#fff;border-radius:3px}
</style>
</head>
<body>

<!-- Top bar -->
<div class="abs topbar">
  <div class="abs phone">
    <svg width="16" height="16" viewBox="0 0 24 24"><path fill="#fff" d="M6.6 10.8a15.1 15.1 0 0 0 6.6 6.6l2.2-2.2c.3-.3.7-.4 1-.2 1.1.4 2.3.6 3.6.6.6 0 1 .4 1 1V20c0 .6-.4 1-1 1A17 17 0 0 1 3 4c0-.6.4-1 1-1h3.5c.6 0 1 .4 1 1 0 1.3.2 2.5.6 3.6.1.3 0 .7-.2 1z"/></svg>
    <span>8012 345 6789</span>
  </div>
  <div class="abs mail">
    <span>info@websitename.com</span>
    <svg width="20" height="14" viewBox="0 0 20 14"><rect x="0.5" y="0.5" width="19" height="13" fill="#fff"/><path d="M1 1l9 7 9-7" stroke="#0b0a4f" fill="none" stroke-width="1.4"/></svg>
  </div>
</div>

<!-- Navigation -->
<nav class="abs nav">
  <a class="active" style="left:73px">HOME</a>
  <a style="left:140px">ABOUT US</a>
  <a style="left:233px">WHO WE ARE</a>
  <a style="left:345px">OUR MISSION</a>
  <a style="left:873px">SERVICES</a>
  <a style="left:958px">OUR TEAM</a>
  <a style="left:1048px">CONTACT US</a>
</nav>
<svg class="abs brand-badge" width="356" height="152" viewBox="0 0 356 152">
  <polygon points="74,0 282,0 356,110 320,152 36,152 0,110" fill="#fff"/>
</svg>
<div class="abs brand-name">SUMMITLINE<br>WEALTH MANAGEMENT</div>

<!-- Hero -->
<div class="abs hero" role="img" aria-label="Two hikers with backpacks on a grassy ridge facing snowy mountains"></div>
<svg class="abs hero-cut" width="1200" height="754" viewBox="0 0 1200 754">
  <polygon points="0,554 600,732 1200,554 1200,754 0,754" fill="#8c8c8c"/>
  <polygon points="0,570 600,748 1200,570 1200,754 0,754" fill="#fff"/>
</svg>
<div class="abs hero-text">
  <div class="kicker">WELCOME TO</div>
  <h1>SUMMITLINE WEALTH<br>MANAGEMENT</h1>
</div>
<a class="btn" style="left:678px;top:527px;width:255px;height:64px;font-size:19px;z-index:2">Learn More <span class="dot"><svg width="10" height="10" viewBox="0 0 10 10"><path d="M3 1l4 4-4 4" stroke="#0b0a4f" stroke-width="2" fill="none"/></svg></span></a>
<div class="abs scroll-dot"><svg width="12" height="16" viewBox="0 0 12 16"><path d="M6 1v13M2 10l4 4 4-4" stroke="#555" stroke-width="1.5" fill="none"/></svg></div>

<!-- About -->
<div class="abs about-photo" role="img" aria-label="Business team portrait collage"></div>
<div class="abs serif sec-title" style="left:676px;top:928px">ABOUT US</div>
<div class="abs sec-sub" style="left:676px;top:982px">Who we are <i style="width:112px"></i></div>
<p class="abs para" style="left:676px;top:1032px;width:446px">Lorem ipsum dolor sit amet, consectetur adipiscing elit. Sed pharetra, turpis vitae tincidunt tempus, ipsum magna varius mauris, et dictum nulla neque ac turpis. Etiam finibus est metus, eu viverra velit auctor ac. Nam luctus lorem felis, quis vulputate quam convallis elementum. Maecenas malesuada risus vitae tristique imperdiet. Interdum et malesuada fames ac ante ipsum primis in faucibus. Cras tristique nunc a tellus semper, et ultrices mauris vulputate.</p>
<a class="btn" style="left:676px;top:1275px;width:186px;height:46px;font-size:14px">Read More <span class="dot"><svg width="8" height="8" viewBox="0 0 10 10"><path d="M3 1l4 4-4 4" stroke="#0b0a4f" stroke-width="2" fill="none"/></svg></span></a>

<!-- Services -->
<svg class="abs services-bg" width="1200" height="1063" viewBox="0 0 1200 1063">
  <polygon points="0,165 600,0 1200,165 1200,1063 0,1063" fill="#f4f4f4"/>
</svg>
<div class="abs serif sec-title" style="left:0;top:1534px;width:1200px;text-align:center">OUR SERVICES</div>
<div class="abs sec-sub" style="left:0;top:1584px;width:1200px;justify-content:center"><i style="width:104px"></i>What we do<i style="width:104px"></i></div>
<p class="abs para" style="left:140px;top:1652px;width:920px;text-align:center">Lorem ipsum dolor sit amet, consectetur adipiscing elit. Sed pharetra, turpis vitae tincidunt tempus, ipsum magna varius mauris, et dictum nulla neque ac turpis. Etiam finibus est metus, eu viverra velit auctor ac.</p>

<div class="abs diamond" style="left:123px;top:1801px"></div>
<div class="abs diamond" style="left:837px;top:1801px"></div>
<div class="abs diamond" style="left:305px;top:1983px"></div>
<div class="abs diamond" style="left:653px;top:1983px"></div>
<div class="abs diamond" style="left:480px;top:1791px;background:var(--navy);z-index:1"></div>

<div class="abs svc" style="left:93px;top:1823px"><div class="icon"><span><svg width="40" height="40" viewBox="0 0 40 40"><rect x="8" y="24" width="5" height="10" fill="#fff"/><rect x="17" y="18" width="5" height="16" fill="#fff"/><rect x="26" y="10" width="5" height="24" fill="#fff"/></svg></span></div><h3>Financial Planning</h3></div>
<div class="abs svc dark" style="left:450px;top:1812px"><div class="icon"><span><svg width="40" height="40" viewBox="0 0 40 40"><path d="M6 22l8-6 6 4 6-4 8 6-8 8h-12z" fill="#fff"/></svg></span></div><h3>Business Planning</h3>
  <div style="margin:16px auto 0;width:90px;height:26px;border-radius:20px;background:#fff;color:var(--navy);font-size:9px;font-weight:600;line-height:26px">READ MORE</div></div>
<div class="abs svc" style="left:807px;top:1823px"><div class="icon"><span><svg width="40" height="40" viewBox="0 0 40 40"><circle cx="20" cy="20" r="11" fill="none" stroke="#fff" stroke-width="4" stroke-dasharray="5 3"/><path d="M20 14l5 9H15z" fill="#fff"/></svg></span></div><h3>Risk Management</h3></div>
<div class="abs svc" style="left:275px;top:2007px"><div class="icon"><span><svg width="40" height="40" viewBox="0 0 40 40"><rect x="8" y="12" width="24" height="16" rx="2" fill="#fff"/><circle cx="20" cy="20" r="4" fill="#0b0a4f"/></svg></span></div><h3>Investment Advising</h3></div>
<div class="abs svc" style="left:623px;top:2007px"><div class="icon"><span><svg width="40" height="40" viewBox="0 0 40 40"><circle cx="15" cy="24" r="6" fill="#fff"/><rect x="24" y="12" width="8" height="18" rx="2" fill="#fff"/></svg></span></div><h3>Retirement Planning</h3></div>

<a class="btn" style="left:506px;top:2296px;width:188px;height:47px;font-size:14px">View More <span class="dot"><svg width="8" height="8" viewBox="0 0 10 10"><path d="M3 1l4 4-4 4" stroke="#0b0a4f" stroke-width="2" fill="none"/></svg></span></a>

<!-- Team -->
<div class="abs serif sec-title" style="left:0;top:2556px;width:1200px;text-align:center">OUR TEAM</div>
<div class="abs sec-sub" style="left:0;top:2607px;width:1200px;justify-content:center"><i style="width:48px"></i>Meet our team<i style="width:50px"></i></div>
<div class="abs card-hi"></div>
<div class="abs member" style="left:118px;top:2728px"><div class="hex"><span role="img" aria-label="Team member portrait"></span></div><h4>Jonathan Hale</h4><p>Lorem ipsum dolor</p><div class="soc"><i></i></div></div>
<div class="abs member" style="left:360px;top:2728px"><div class="hex"><span role="img" aria-label="Team member portrait"></span></div><h4>Stephen Kerr</h4><p>Lorem ipsum dolor</p><div class="soc"><i></i></div></div>
<div class="abs member" style="left:603px;top:2728px"><div class="hex"><span role="img" aria-label="Team member portrait"></span></div><h4>Dara Dennison</h4><p>Lorem ipsum dolor</p><div class="soc"><i></i></div></div>
<div class="abs member" style="left:846px;top:2728px"><div class="hex"><span role="img" aria-label="Team member portrait"></span></div><h4>Wendell Price</h4><p>Lorem ipsum dolor</p><div class="soc"><i></i></div></div>
<a class="btn" style="left:506px;top:3140px;width:188px;height:47px;font-size:14px">View More <span class="dot"><svg width="8" height="8" viewBox="0 0 10 10"><path d="M3 1l4 4-4 4" stroke="#0b0a4f" stroke-width="2" fill="none"/></svg></span></a>

<!-- Contact -->
<div class="abs contact"></div>
<div class="abs" style="left:142px;top:3430px;font-family:'Cinzel',serif;font-size:48px;color:#fff">CONTACT US</div>
<div class="abs sec-sub" style="left:144px;top:3482px;color:#fff">Get in touch with <i style="width:128px;background:#fff"></i></div>
<div class="abs field" style="left:144px;top:3558px;width:198px;height:38px">First Name:</div>
<div class="abs field" style="left:361px;top:3558px;width:197px;height:38px">Last Name:</div>
<div class="abs field" style="left:144px;top:3615px;width:198px;height:39px">Phone:</div>
<div class="abs field" style="left:361px;top:3615px;width:197px;height:39px">Email:</div>
<div class="abs field" style="left:144px;top:3674px;width:414px;height:125px;padding-top:18px">Mesage:</div>
<a class="btn light" style="left:144px;top:3836px;width:189px;height:48px;font-size:14px">Submit Now <span class="dot"><svg width="8" height="8" viewBox="0 0 10 10"><path d="M3 1l4 4-4 4" stroke="#fff" stroke-width="2" fill="none"/></svg></span></a>
<svg class="abs" style="left:600px;top:3434px" width="460" height="448" viewBox="0 0 460 448">
  <defs><linearGradient id="officeTone" x1="0" y1="0" x2="1" y2="1"><stop offset="0" stop-color="#e9edf2"/><stop offset="0.6" stop-color="#9ea6b2"/><stop offset="1" stop-color="#2a2d38"/></linearGradient></defs>
  <polygon points="232,2 458,446 2,446" fill="none" stroke="#fff" stroke-width="2"/>
  <polygon role="img" aria-label="Businessman reading documents at an office desk" points="232,40 430,440 40,440" fill="url(#officeTone)"/>
</svg>

<!-- Footer -->
<svg class="abs footer-bg" width="1200" height="444" viewBox="0 0 1200 444">
  <polygon points="0,130 640,12 1200,130 1200,444 0,444" fill="#f4f4f4"/>
</svg>
<div class="abs footer" style="left:95px;top:4240px;width:240px;text-align:center;font-family:'Cinzel',serif;color:var(--navy);font-size:20px;line-height:25px">SUMMITLINE<br>WEALTH MANAGEMENT</div>

<div class="abs footer foot-title" style="left:416px;top:4152px">QUICK LINKS</div>
<ul class="abs footer links" style="left:416px;top:4214px">
  <li>About Us</li><li>Who We Are</li><li>Our Mission</li><li>Services</li><li>Our Team</li><li>Contact Us</li>
</ul>

<div class="abs footer foot-title" style="left:629px;top:4152px">CONTACT US</div>
<div class="abs footer" style="left:629px;top:4220px;display:flex;flex-direction:column;gap:16px">
  <div class="c-item"><span class="c-ico"></span><div><b>CALL US</b><br>8012 345 6789</div></div>
  <div class="c-item"><span class="c-ico"></span><div><b>EMAIL US</b><br>info@websitename.com</div></div>
  <div class="c-item"><span class="c-ico"></span><div>Address Line Dummy here<br>Address line dummy</div></div>
</div>

<div class="abs footer foot-title" style="left:910px;top:4152px">OUR NEWSLETTER</div>
<p class="abs footer" style="left:910px;top:4216px;width:210px;font-size:13.5px;line-height:17px;color:#222">Subscribe our newsletter to get the latest news.</p>
<div class="abs footer" style="left:910px;top:4275px;width:195px;height:28px;background:#fff;border:1px solid #ddd"></div>
<div class="abs footer" style="left:910px;top:4320px;width:97px;height:28px;background:var(--navy);color:#fff;font-size:10px;line-height:28px;text-align:center">SUBSCRIBE</div>

<div class="abs bottom">
  <div class="abs" style="left:69px;top:18px">Copyright © 2024 All Rights Reserved By Company name</div>
  <div class="abs" style="left:1016px;top:14px;display:flex;gap:6px"><span class="sq"></span><span class="sq"></span><span class="sq"></span><span class="sq"></span></div>
</div>

</body>
</html>
```